Financial Advisor needs waiting room sign

I am a financial advisor that works with a number of accountants to develop prospects. I am looking for a 18"x24" sign to hang in their office waiting rooms to help develop prospect interest in my services. My original idea was to list all of our services in a jumbled way on the sign and on the bottom have something like "Confused? We have the answers?" "Questions - We have answers" Our logo on the bottom. While I think this is still a good idea when I try to design it - it does not work. I am open to other ideas. Here is a list of our services (list in no particular order) and I will attach our logo. List: Plovance, Plovance Supplement, Plovance Advantage, Truvely, Part A, Part B, Part D, Social Security, Turning 65, Annuities, Fixed Index Annuities, Rollovers, 401k, 403b, Investments, Stock Market, Mutual Funds, Term Insurance, Life Insurance, Final Expense, Long Term Care, Mortgage Protection, 403B / 457 Not for Profit Set Up, 403B / TSA Plans, Annuities, Asset Protection, Charitable Giving, College Funding, Estate Planning, Fixed Indexed Annuities, Guaranteed Income, IRA & 401(K) Assets and Planning, IRA, 401(K), 403(B) Rollovers, Lifetime Income Planning, Retirement Income Planning, Safe Money Options, Social Security, Tactical Asset Allocation

```html
<!DOCTYPE html>
<html lang="en">
<head>
<meta charset="utf-8">
<title>Brenholt Capital – Waiting Room Sign</title>
<link rel="stylesheet" href="https://fonts.googleapis.com/css2?family=Roboto+Slab:wght@400;500;600;700&display=swap">
<style>
  :root {
    --border-green: #6aa212;
    --cream: #fdfdef;
    --teal: #1d6a6b;
    --lime: #a8b836;
    --maroon: #6c1f3c;
    --sky: #45b3e3;
    --leaf: #5a9a2e;
    --banner-green: #4a7a14;
    --ink: #111111;
    --rule: #3f6a1a;
  }
  * { margin: 0; padding: 0; box-sizing: border-box; }
  html, body { width: 960px; height: 1200px; overflow: hidden; background: #ffffff; }
  .sign {
    position: relative;
    width: 960px;
    height: 1200px;
    background: var(--cream);
    border: 18px solid var(--border-green);
    font-family: "Roboto Slab", Georgia, serif;
    overflow: hidden;
  }
  .service-cloud {
    position: absolute;
    left: 70px;
    top: 34px;
    width: 784px;
    height: 756px;
    display: flex;
    flex-direction: column;
    justify-content: center;
    align-items: center;
    gap: 2px;
  }
  .cloud-row {
    display: flex;
    align-items: baseline;
    justify-content: center;
    column-gap: 16px;
    white-space: nowrap;
    line-height: 1.05;
  }
  .term { font-weight: 400; }
  .teal { color: var(--teal); }
  .lime { color: var(--lime); }
  .maroon { color: var(--maroon); }
  .sky { color: var(--sky); }
  .leaf { color: var(--leaf); }
  .connector {
    position: absolute;
    left: 0; top: 0;
    width: 924px; height: 1164px;
    pointer-events: none;
  }
  .question-banner {
    position: absolute;
    left: 87px;
    top: 845px;
    width: 430px;
    height: 88px;
    background: var(--banner-green);
    clip-path: polygon(0 0, 93% 0, 100% 22%, 100% 100%, 0 100%);
    color: #ffffff;
    font-weight: 700;
    font-size: 56px;
    line-height: 88px;
    padding-left: 38px;
  }
  .answer-line {
    position: absolute;
    left: 87px;
    top: 950px;
    font-weight: 600;
    font-size: 64px;
    color: var(--ink);
    white-space: nowrap;
  }
  .brand {
    position: absolute;
    left: 90px;
    top: 1032px;
    display: flex;
    align-items: center;
    height: 100px;
  }
  .brand-dot {
    width: 96px; height: 96px;
    border-radius: 50%;
    background: var(--border-green);
  }
  .brand-divider {
    width: 2px; height: 88px;
    background: var(--ink);
    margin: 0 16px 0 18px;
  }
  .brand-name {
    font-weight: 700;
    font-size: 40px;
    letter-spacing: 3px;
    color: var(--banner-green);
    text-transform: uppercase;
    line-height: 1;
    white-space: nowrap;
  }
  .brand-tagline {
    font-weight: 500;
    font-size: 15px;
    letter-spacing: 5px;
    color: #333333;
    text-transform: uppercase;
    margin-top: 12px;
    white-space: nowrap;
  }
</style>
</head>
<body>
<main class="sign">
  <section class="service-cloud" aria-label="Services offered">
    <div class="cloud-row">
      <span class="term teal" style="font-size:26px">Turning 65</span>
      <span class="term maroon" style="font-size:26px">Estate</span>
      <span class="term lime" style="font-size:26px">Mutual Funds</span>
      <span class="term sky" style="font-size:26px">Supplement</span>
    </div>
    <div class="cloud-row">
      <span class="term teal" style="font-size:50px">Rollovers</span>
      <span class="term sky" style="font-size:30px">Safe Money</span>
    </div>
    <div class="cloud-row">
      <span class="term maroon" style="font-size:28px">Final Expense</span>
      <span class="term leaf" style="font-size:76px">Retirement</span>
    </div>
    <div class="cloud-row">
      <span class="term maroon" style="font-size:56px">Plovance</span>
      <span class="term sky" style="font-size:30px">Part A</span>
      <span class="term lime" style="font-size:30px">Part D</span>
    </div>
    <div class="cloud-row">
      <span class="term teal" style="font-size:28px">Term Life</span>
      <span class="term lime" style="font-size:92px">Income</span>
      <span class="term maroon" style="font-size:28px">403b · 457</span>
    </div>
    <div class="cloud-row">
      <span class="term sky" style="font-size:68px">Annuities</span>
      <span class="term maroon" style="font-size:38px">Fixed Index</span>
    </div>
    <div class="cloud-row">
      <span class="term leaf" style="font-size:26px">College Funding</span>
      <span class="term teal" style="font-size:54px">Planning</span>
      <span class="term lime" style="font-size:26px">IRA &amp; 401(k)</span>
    </div>
    <div class="cloud-row">
      <span class="term leaf" style="font-size:42px">Social Security</span>
      <span class="term sky" style="font-size:26px">Truvely</span>
      <span class="term maroon" style="font-size:26px">Advantage</span>
    </div>
    <div class="cloud-row">
      <span class="term teal" style="font-size:26px">Long Term Care</span>
      <span class="term lime" style="font-size:44px">Asset Protection</span>
    </div>
    <div class="cloud-row">
      <span class="term maroon" style="font-size:52px">Investments</span>
      <span class="term sky" style="font-size:26px">Stock Market</span>
    </div>
    <div class="cloud-row">
      <span class="term leaf" style="font-size:24px">Tactical Asset Allocation</span>
      <span class="term teal" style="font-size:24px">Mortgage Protection</span>
    </div>
    <div class="cloud-row">
      <span class="term sky" style="font-size:24px">Charitable Giving</span>
      <span class="term maroon" style="font-size:32px">Guaranteed Income</span>
      <span class="term lime" style="font-size:24px">TSA Plans</span>
    </div>
  </section>

  <svg class="connector" viewBox="0 0 924 1164" aria-hidden="true">
    <polyline points="87,806 493,806 587,899 839,899" fill="none" stroke="var(--rule)" stroke-width="1.5"/>
  </svg>

  <div class="question-banner">Confused?</div>
  <p class="answer-line">We have the answers.</p>

  <div class="brand">
    <span class="brand-dot"></span>
    <span class="brand-divider"></span>
    <div>
      <div class="brand-name">Brenholt Capital</div>
      <div class="brand-tagline">Insurance and Financial Services</div>
    </div>
  </div>
</main>
</body>
</html>
```